'TOLVANTA' NEW WINE LABEL DESIGN

I am looking for an exceptional and exciting design for a wine label called 'Tolvanta' meaning 'Lookout'. The design must feature the name 'Tolvanta', and the word 'Cabernet Sauvignon' in version 1 and 'Sauvignon Blanc' in version 2. It will also need the words 'Valle Central, Chile' at the bottom of the label as a prominent piece of information as well as the vintage 2017. Please produce the work in size 80mm x 100mm. Feel free to use colour in addition to black/white and ensue that the label is easy to read on a shelf placement.
Target Market(s)
SUPERMARKETS & WINE STORES
Requirements
Must have
- EASY TO READ, USE COLOURS LIKE GREEN FOR SAUVIGNON & RED FOR CABERNET SAUVIGNON
- FULL BOTTLE SHOT MUST BE IN PROVIDED DESIGNS. ALL BOTTLE TOPS SHOULD BE QUORLAN STYLE (SCREW TOP)
- PLEASE NOTE THAT LABEL INFORMATION MUSY BE EASY TO READ I.E. VINTAGE, PLACE OF ORGIN ALTHOUGH NOT THE MAIN CONTENT MUST STILL BE CLEAR.
Nice to have
- ARTISTIC REFERENCE LINK TO NAME & ANDES BUT NOT PICTURES OF MOUNTAINS
Should not have
- PICTURES OF GRAPES
- PICTURES OF VINEYARDS
- PICTURES OF MOUNTAINS

```html
<!DOCTYPE html>
<html lang="en">
<head>
<meta charset="utf-8">
<title>Tolvanta Wine Labels</title>
<link rel="stylesheet" href="https://fonts.googleapis.com/css2?family=Playfair+Display:wght@400;500&family=Oswald:wght@300&family=Libre+Baskerville&display=swap">
<style>
  :root {
    --backdrop: #dcdcdc;
    --label-paper: #fbfbfa;
    --ink: #141414;
    --cabernet-red: #b3192f;
    --sauvignon-green: #8ba83a;
    --artwork-mid: #e6e6e4;
    --artwork-deep: #c9c9c7;
  }
  * { box-sizing: border-box; margin: 0; padding: 0; }
  html, body {
    width: 1200px;
    height: 1057px;
    overflow: hidden;
    background: var(--backdrop);
  }
  .label-range {
    display: flex;
    justify-content: center;
    align-items: center;
    gap: 80px;
    width: 1200px;
    height: 1057px;
  }
  .wine-label {
    position: relative;
    width: 480px;
    height: 566px;
    background: var(--label-paper);
    box-shadow: 0 2px 10px rgba(0,0,0,0.08);
    color: var(--ink);
    text-align: center;
    overflow: hidden;
  }
  .brand-name {
    position: absolute;
    top: 82px;
    left: 0;
    right: 0;
    font-family: "Playfair Display", serif;
    font-weight: 500;
    font-size: 66px;
    line-height: 1;
  }
  .grape-variety {
    position: absolute;
    top: 152px;
    left: 0;
    right: 0;
    font-family: "Oswald", sans-serif;
    font-weight: 300;
    font-size: 24px;
    line-height: 1;
  }
  .grape-variety--cabernet { color: var(--cabernet-red); }
  .grape-variety--blanc { color: var(--sauvignon-green); }
  .ridge-artwork {
    position: absolute;
    top: 228px;
    left: 0;
    width: 480px;
    height: 196px;
    background: radial-gradient(ellipse 70% 95% at 50% 100%,
      var(--artwork-deep) 0%,
      var(--artwork-mid) 50%,
      var(--label-paper) 100%);
  }
  .origin {
    position: absolute;
    top: 452px;
    left: 0;
    right: 0;
    font-family: "Libre Baskerville", serif;
    font-size: 16px;
    line-height: 1;
  }
  .vintage {
    position: absolute;
    top: 484px;
    left: 0;
    right: 0;
    font-family: "Libre Baskerville", serif;
    font-size: 38px;
    line-height: 1;
  }
</style>
</head>
<body>
  <main class="label-range">
    <section class="wine-label">
      <h1 class="brand-name">TOLVANTA</h1>
      <p class="grape-variety grape-variety--cabernet">Cabernet Sauvignon</p>
      <div class="ridge-artwork" role="img" aria-label="Black line drawing of overlapping peaks across the label"></div>
      <p class="origin">Valle Central, Chile</p>
      <p class="vintage">2017</p>
    </section>
    <section class="wine-label">
      <h1 class="brand-name">TOLVANTA</h1>
      <p class="grape-variety grape-variety--blanc">Sauvignon Blanc</p>
      <div class="ridge-artwork" role="img" aria-label="Black line drawing of overlapping peaks across the label"></div>
      <p class="origin">Valle Central, Chile</p>
      <p class="vintage">2017</p>
    </section>
  </main>
</body>
</html>
```